Email Signiture and letterhead design

we are looking for a modern business design to incorporate our logo and iso certification plus social icons for Twitter, LinkedIn, and youtube
they must include our UK vat and also company registration as text but I can fill these out. Email signature to have a link/icon to our webshop www.dremlox.co.uk

Target Market(s)

All

Font styles to use
Serif
Sans Serif

Requirements
Must have
• Address, tel, email , web details incorperated
Nice to have
• a professional looking letter head and email signiture, Email signature to have a link/icon to our webshop www.dremlox.co.uk

```html
<!DOCTYPE html>
<html lang="en">
<head>
<meta charset="utf-8">
<title>Dremlox Hubs &amp; Bearings Ltd — Letterhead</title>
<link href="https://fonts.googleapis.com/css2?family=Lato:wght@400;700&display=swap" rel="stylesheet">
<style>
  :root {
    --backdrop: #dedede;
    --paper: #f2f2f3;
    --ink: #1d1d2b;
    --body: #45454f;
    --muted: #5a5a62;
    --brand-red: #d0121b;
    --header-grey: #c9c9cc;
    --rule: #9a9aa0;
    --badge-pink: #c2126f;
  }
  * { box-sizing: border-box; margin: 0; padding: 0; }
  html, body { width: 1200px; height: 1012px; overflow: hidden; }
  body {
    background: var(--backdrop);
    font-family: "Lato", Arial, sans-serif;
    color: var(--body);
    position: relative;
  }
  .letterhead {
    position: absolute;
    left: 257px; top: 17px;
    width: 686px; height: 978px;
    background: var(--paper);
    box-shadow: 0 6px 24px rgba(0,0,0,0.18);
    overflow: hidden;
  }
  .header-accent {
    position: absolute; right: 0; top: 0;
    width: 240px; height: 110px;
    background: radial-gradient(ellipse at 100% 0%, var(--header-grey) 0%, rgba(201,201,204,0.45) 45%, rgba(242,242,243,0) 75%);
  }
  .brand {
    position: absolute; left: 41px; top: 84px;
    display: flex; align-items: center; gap: 8px;
  }
  .brand-dot { width: 14px; height: 14px; border-radius: 50%; background: var(--brand-red); }
  .brand-name { font-weight: 700; font-size: 14px; color: var(--brand-red); letter-spacing: 0.3px; }
  .letter-date { position: absolute; right: 86px; top: 84px; font-size: 11.5px; color: var(--muted); }
  .salutation { position: absolute; left: 73px; top: 200px; font-weight: 700; font-size: 14.5px; color: var(--ink); }
  .letter-body { position: absolute; left: 73px; top: 261px; width: 532px; }
  .letter-body p {
    font-size: 11.3px; line-height: 20.6px; letter-spacing: 0.62px;
    color: var(--body); margin-bottom: 20.6px;
  }
  .closing { position: absolute; left: 73px; top: 647px; font-size: 11px; color: var(--muted); }
  .signature {
    position: absolute; left: 73px; top: 693px; width: 182px; height: 48px;
    background: linear-gradient(90deg, #e4e4e8, #ececef);
    border-radius: 3px;
  }
  .signatory { position: absolute; left: 73px; top: 746px; font-size: 11px; line-height: 18px; color: var(--muted); }
  .signatory .name { text-transform: uppercase; }
  .footer-rule { position: absolute; left: 41px; top: 848px; width: 610px; height: 1px; background: var(--rule); }
  .footer-about {
    position: absolute; left: 41px; top: 860px; width: 612px;
    font-size: 7.6px; line-height: 12.8px; color: var(--ink);
  }
  .footer-contacts {
    position: absolute; left: 41px; top: 912px;
    display: flex; gap: 24px; font-size: 7.6px; color: var(--ink);
  }
  .contact { display: flex; align-items: center; gap: 5px; }
  .contact svg { flex: none; }
  .footer-social { position: absolute; left: 41px; top: 942px; display: flex; align-items: center; gap: 11px; }
  .social-dot { width: 20px; height: 20px; border-radius: 50%; background: var(--brand-red); }
  .social-tag { font-size: 8.5px; font-weight: 700; color: var(--brand-red); }
  .iso-badge {
    position: absolute; left: 522px; top: 904px; width: 137px; height: 50px;
    border: 2px solid var(--ink); border-radius: 9px; background: #fff; overflow: hidden;
  }
  .iso-badge::after {
    content: ""; position: absolute; right: 0; top: 0; width: 14px; height: 100%; background: var(--badge-pink);
  }
  .certificate-no {
    position: absolute; left: 522px; top: 957px; width: 128px;
    text-align: center; font-size: 6px; color: var(--ink);
  }
</style>
</head>
<body>
  <main class="letterhead">
    <div class="header-accent" role="img" aria-label="Soft grey decorative header curves"></div>

    <div class="brand">
      <span class="brand-dot"></span>
      <span class="brand-name">Dremlox Hubs &amp; Bearings Ltd</span>
    </div>
    <p class="letter-date">London 28th. April 2023</p>

    <h1 class="salutation">Dear Jordan Ellis,</h1>

    <section class="letter-body">
      <p>Lorem ipsum dolor sit amet, consectetur adipiscing elit, sed do eiusmod tempor incididunt ut labore et dolore magna aliqua. Ut enim ad minim veniam, quis nostrud exercitation ullamco laboris nisi ut aliquip ex ea commodo consequat. Duis aute irure dolor in reprehenderit in voluptate velit esse cillum dolore eu fugiat nulla pariatur. Excepteur sint occaecat cupidatat non proident, sunt in culpa qui officia deserunt mollit anim id est laborum.</p>
      <p>Sed ut perspiciatis unde omnis iste natus error sit voluptatem accusantium doloremque laudantium, totam rem aperiam, eaque ipsa quae ab illo inventore veritatis et quasi architecto beatae vitae dicta sunt explicabo. Sed do eiusmod tempor incididunt ut labore et dolore magna aliqua.</p>
      <p>Excepteur sint occaecat cupidatat non proident, sunt in culpa qui officia deserunt mollit anim id est laborum. Lorem ipsum dolor sit amet, consectetur adipiscing elit, sed do eiusmod tempor incididunt ut labore et dolore magna aliqua. Ut enim ad minim veniam, quis nostrud exercitation ullamco laboris nisi ut aliquip.</p>
    </section>

    <p class="closing">Sincerely,</p>
    <div class="signature" role="img" aria-label="Handwritten signature of Martin Hale"></div>
    <div class="signatory">
      <p class="name">Martin Hale</p>
      <p class="role">General Manager</p>
    </div>

    <div class="footer-rule"></div>
    <p class="footer-about">We are the leading experts in HGV wheel hubs and bearings. With support from OEM suppliers, our dedicated and highly trained team of technicians will have your HGV wheel hubs and bearings repaired, exchanged, or replaced ASAP. We aim for minimum disruption to your business and understand the immediacy for getting your vehicle<br>TAX reference: 48K902317</p>

    <div class="footer-contacts">
      <span class="contact">
        <svg width="8" height="10" viewBox="0 0 8 10" aria-hidden="true"><path d="M4 0a4 4 0 0 0-4 4c0 3 4 6 4 6s4-3 4-6a4 4 0 0 0-4-4zm0 5.5a1.5 1.5 0 1 1 0-3 1.5 1.5 0 0 1 0 3z" fill="var(--ink)"/></svg>
        Calder Row, Ashfield Park, Manchester, M40 2QT
      </span>
      <span class="contact">
        <svg width="9" height="9" viewBox="0 0 24 24" aria-hidden="true"><path d="M6.6 10.8a15 15 0 0 0 6.6 6.6l2.2-2.2a1 1 0 0 1 1-.25 11.4 11.4 0 0 0 3.6.57 1 1 0 0 1 1 1V20a1 1 0 0 1-1 1A17 17 0 0 1 3 4a1 1 0 0 1 1-1h3.5a1 1 0 0 1 1 1c0 1.25.2 2.45.57 3.57a1 1 0 0 1-.25 1z" fill="var(--ink)"/></svg>
        +44 (0) 161 555 0148
      </span>
      <span class="contact"><b>@</b> info@dremlox.co.uk</span>
    </div>

    <div class="footer-social">
      <span class="social-dot" aria-label="Video channel link"></span>
      <span class="social-dot" aria-label="News feed link"></span>
      <span class="social-dot" aria-label="Professional profile link"></span>
      <span class="social-tag">#dremlox</span>
    </div>

    <div class="iso-badge" aria-label="Quality management certification badge"></div>
    <p class="certificate-no">Certificate No:481207365</p>
  </main>
</body>
</html>
```